BOLD & MINIMALIST DESIGN NEEDED

We want a very bold but minimalistic business card design that is impactful and utilizes both sides of the business card. Our current logo is included for your use.

We want bold fonts and good use of negative space. We don't want the logo to overpower the design.

Target Market(s)

Professionals who are building new commercial buildings.

Industry/Entity Type

Construction

Contact Information for Business Card

Name, Title, email, office phone, cell phone, website

Font styles to use
Serif
Sans Serif

Requirements
Must have
• Bold design!

```html
<!DOCTYPE html>
<html lang="en">
<head>
<meta charset="utf-8">
<title>Ridgeline Business Card</title>
<link rel="stylesheet" href="https://fonts.googleapis.com/css2?family=Montserrat:wght@500;600;700&family=Inter:wght@400&display=swap">
<style>
  :root {
    --backdrop: #546564;
    --navy: #00022d;
    --paper: #ffffff;
    --ink: #2f2a2a;
    --text-light: #ffffff;
    --icon-tile: #d8d4c8;
    --icon-disc: #1f4890;
  }
  html, body {
    margin: 0;
    padding: 0;
    width: 1200px;
    height: 1200px;
    overflow: hidden;
    background: var(--backdrop);
  }
  .canvas {
    position: relative;
    width: 1200px;
    height: 1200px;
    background: var(--backdrop);
  }
  .card {
    position: absolute;
    left: 0;
    top: 300px;
    width: 1200px;
    height: 600px;
    background: var(--paper);
    overflow: hidden;
  }
  .card__bands {
    position: absolute;
    inset: 0;
  }
  .person {
    position: absolute;
    left: 0;
    width: 274px;
    text-align: center;
    color: var(--text-light);
  }
  .person__name {
    position: absolute;
    top: 96px;
    width: 100%;
    font-family: "Montserrat", sans-serif;
    font-weight: 600;
    font-size: 52px;
    letter-spacing: 5px;
    line-height: 1;
  }
  .person__title {
    position: absolute;
    top: 156px;
    width: 100%;
    font-family: "Montserrat", sans-serif;
    font-weight: 700;
    font-size: 28px;
    letter-spacing: 5px;
    line-height: 1;
  }
  .person__phone {
    position: absolute;
    top: 220px;
    width: 100%;
    font-family: "Inter", Arial, sans-serif;
    font-size: 29px;
    line-height: 1;
  }
  .brand {
    position: absolute;
    left: 0;
    width: 1200px;
    top: 258px;
    display: flex;
    justify-content: center;
    align-items: center;
    gap: 16px;
    padding-right: 18px;
    box-sizing: border-box;
  }
  .brand__mark {
    width: 34px;
    height: 34px;
    background: var(--ink);
  }
  .brand__name {
    font-family: "Montserrat", sans-serif;
    font-weight: 700;
    font-size: 52px;
    color: var(--ink);
    letter-spacing: 1px;
    line-height: 1;
  }
  .office {
    position: absolute;
    right: 40px;
    top: 372px;
    font-family: "Montserrat", sans-serif;
    font-weight: 600;
    font-size: 22px;
    letter-spacing: 3px;
    color: var(--text-light);
    transform: scaleX(1.5);
    transform-origin: right center;
    line-height: 1;
  }
  .contact {
    position: absolute;
    right: 39px;
    display: flex;
    align-items: center;
    gap: 25px;
    color: var(--text-light);
    font-family: "Inter", Arial, sans-serif;
  }
  .contact__text { line-height: 1; }
  .contact--phone { top: 427px; }
  .contact--phone .contact__text { font-size: 17px; letter-spacing: 3px; }
  .contact--web { top: 473px; }
  .contact--web .contact__text { font-size: 14px; }
  .contact--address { top: 520px; }
  .contact--address .contact__text { font-size: 19px; }
  .contact__icon {
    width: 30px;
    height: 29px;
    display: block;
  }
</style>
</head>
<body>
<main class="canvas">
  <section class="card">
    <svg class="card__bands" width="1200" height="600" viewBox="0 0 1200 600" aria-hidden="true">
      <polygon points="0,0 364,0 133,600 0,600" fill="var(--navy)"/>
      <polygon points="1050,0 1200,0 1200,600 818,600" fill="var(--navy)"/>
    </svg>

    <div class="person">
      <div class="person__name">NAME</div>
      <div class="person__title">TITLE</div>
      <div class="person__phone">+123456789</div>
    </div>

    <div class="brand">
      <span class="brand__mark"></span>
      <span class="brand__name">RIDGELINE</span>
    </div>

    <div class="office">office</div>

    <div class="contact contact--phone">
      <span class="contact__text">+123456789</span>
      <svg class="contact__icon" viewBox="0 0 30 29" aria-hidden="true">
        <rect width="30" height="29" fill="var(--icon-tile)"/>
        <circle cx="15" cy="14.5" r="11" fill="var(--icon-disc)"/>
        <path d="M11 9.5c.6-.6 1.4-.5 1.8.2l1 1.7c.3.5.2 1.1-.2 1.5l-.7.6c.7 1.5 1.8 2.6 3.3 3.3l.6-.7c.4-.4 1-.5 1.5-.2l1.7 1c.7.4.8 1.2.2 1.8l-.8.8c-.9.9-2.3 1-3.4.4-2.5-1.3-4.5-3.3-5.8-5.8-.6-1.1-.5-2.5.4-3.4z" fill="var(--text-light)"/>
      </svg>
    </div>

    <div class="contact contact--web">
      <span class="contact__text">www.ridgelinebuild.com</span>
      <svg class="contact__icon" viewBox="0 0 30 29" aria-hidden="true">
        <rect width="30" height="29" fill="var(--icon-tile)"/>
        <circle cx="15" cy="14.5" r="11" fill="var(--icon-disc)"/>
        <g fill="none" stroke="var(--text-light)" stroke-width="1.1">
          <circle cx="15" cy="14.5" r="6"/>
          <ellipse cx="15" cy="14.5" rx="2.6" ry="6"/>
          <line x1="9" y1="14.5" x2="21" y2="14.5"/>
        </g>
      </svg>
    </div>

    <div class="contact contact--address">
      <span class="contact__text">1234 anywhere st</span>
      <svg class="contact__icon" viewBox="0 0 30 29" aria-hidden="true">
        <rect width="30" height="29" fill="var(--icon-tile)"/>
        <circle cx="15" cy="14.5" r="11" fill="var(--icon-disc)"/>
        <path d="M15 7.5c-2.6 0-4.5 2-4.5 4.4 0 3.2 4.5 8.3 4.5 8.3s4.5-5.1 4.5-8.3c0-2.4-1.9-4.4-4.5-4.4z" fill="var(--text-light)"/>
        <circle cx="15" cy="11.9" r="1.6" fill="var(--icon-disc)"/>
      </svg>
    </div>
  </section>
</main>
</body>
</html>
```